Business Card for Mortuary

We need a business card design for our mortuary. We are not the "traditional" mortuary and specialize in simple cremations and burials. We use a two sided card.

Industry/Entity Type

Funeral Home

Contact Information for Business Card

One side we would like to have with the general information of the mortuary:
Address: 4127 E. Larkspur Ave, Sun City, AZ 85399
Phone: 623-555-0142
email: hello@willowbendmortuary.example
website: willowbendmortuary.example

On the other side would like to have the information of employee:
Name: Mark T. Ellis
Email: mark@willowbendmortuary.example
Title: Funeral Director
Text: 602-555-0187

Font styles to use
Serif
Sans Serif

Requirements
Should not have
• Do not put any gothic images or things like a hearse or tombstone.

```html
<!DOCTYPE html>
<html lang="en">
<head>
<meta charset="utf-8">
<title>Willowbend Mortuary – Business Card</title>
<link rel="stylesheet" href="https://fonts.googleapis.com/css2?family=Roboto:wght@400;500;700&display=swap">
<style>
  :root {
    --green: #82bc41;
    --ink: #111111;
    --text-grey: #4a4a4a;
    --paper: #ffffff;
    --backdrop: #e6e6e6;
  }
  * { margin: 0; padding: 0; box-sizing: border-box; }
  html, body { width: 1200px; height: 1200px; overflow: hidden; }
  body {
    background: var(--backdrop);
    font-family: "Roboto", Arial, sans-serif;
    position: relative;
  }
  .card {
    position: absolute;
    left: 255px;
    width: 690px;
    height: 392px;
    border-radius: 22px;
    overflow: hidden;
  }
  .card-front { top: 150px; background: var(--paper); }
  .card-back { top: 645px; background: var(--green); }

  .front-base {
    position: absolute; left: 0; right: 0; bottom: 0; height: 20px;
    background: var(--green);
    border-top: 3px solid var(--ink);
  }

  .brand { position: absolute; display: flex; align-items: center; }
  .brand-dot { border-radius: 50%; flex: none; }
  .brand-name { font-weight: 700; color: var(--ink); white-space: nowrap; }

  .card-front .brand { left: 58px; top: 166px; }
  .card-front .brand-dot { width: 34px; height: 34px; background: var(--green); margin-right: 12px; }
  .card-front .brand-name { font-size: 22px; }

  .divider {
    position: absolute; left: 355px; top: 92px; width: 1px; height: 206px;
    background: var(--ink);
  }
  .contact { position: absolute; left: 374px; top: 94px; color: var(--text-grey); }
  .contact-name { font-size: 24px; font-weight: 700; color: var(--green); line-height: 1.2; }
  .contact-title { font-size: 15.5px; font-weight: 500; color: var(--ink); margin-bottom: 12px; }
  .contact-address { font-size: 15.5px; line-height: 1.3; margin-bottom: 10px; }
  .contact-list { list-style: none; font-size: 15.5px; line-height: 1.27; }
  .contact-list li { display: flex; align-items: center; gap: 8px; }
  .contact-list svg { width: 13px; height: 13px; flex: none; fill: var(--green); }

  .card-back .brand { left: 0; right: 0; top: 166px; justify-content: center; }
  .card-back .brand-dot { width: 58px; height: 58px; background: var(--paper); margin-right: 18px; }
  .card-back .brand-name { font-size: 40px; }

  .back-url {
    position: absolute; left: 0; right: 0; top: 340px;
    text-align: center; font-size: 15px; letter-spacing: 3px; color: var(--ink);
  }
</style>
</head>
<body>
  <section class="card card-front">
    <div class="brand">
      <span class="brand-dot"></span>
      <div class="brand-name">Willowbend Mortuary</div>
    </div>

    <div class="divider"></div>

    <div class="contact">
      <p class="contact-name">Mark T. Ellis</p>
      <p class="contact-title">Funeral Director</p>
      <p class="contact-address">4127 E. Larkspur Ave,<br>Sun City, AZ 85399</p>
      <ul class="contact-list">
        <li><svg viewBox="0 0 16 16"><path d="M3.6 1 6 3.6 4.7 5.6a9 9 0 0 0 5.7 5.7l2-1.3L15 12.4 13.6 15C6.8 15 1 9.2 1 2.4z"/></svg>602-555-0187</li>
        <li><svg viewBox="0 0 16 16"><path d="M3.6 1 6 3.6 4.7 5.6a9 9 0 0 0 5.7 5.7l2-1.3L15 12.4 13.6 15C6.8 15 1 9.2 1 2.4z"/></svg>623-555-0142</li>
        <li><svg viewBox="0 0 16 16"><path d="M1 4h14v9H1zM1 4l7 5 7-5" stroke="#fff" stroke-width="1.2"/></svg>mark@willowbendmortuary.example</li>
        <li><svg viewBox="0 0 16 16"><path d="M1 4h14v9H1zM1 4l7 5 7-5" stroke="#fff" stroke-width="1.2"/></svg>hello@willowbendmortuary.example</li>
        <li><svg viewBox="0 0 16 16"><circle cx="8" cy="8" r="7"/><path d="M1 8h14M8 1c-3 3.5-3 10.5 0 14M8 1c3 3.5 3 10.5 0 14" stroke="#fff" stroke-width="1" fill="none"/></svg>willowbendmortuary.example</li>
      </ul>
    </div>

    <div class="front-base"></div>
  </section>

  <section class="card card-back">
    <div class="brand">
      <span class="brand-dot"></span>
      <div class="brand-name">Willowbend Mortuary</div>
    </div>
    <p class="back-url">www.willowbendmortuary.example</p>
  </section>
</body>
</html>
```